Process Graphic for website

We would like to design a graphic that shows our internal process for scanning our customer records. Our process is listed in order below:
Transport Documents
Inventory Records
Document Preparation
Scan Documents
AI & Data Extraction
Quality Control
Deliver Documents
Records Retention or Destruction

Our customers need to know that we have a clear defined process for scanning records and it needs to visually demonstrate that in a simple way. I have attached our logo as these are the colors of our new website so whatever colors you chose should match our site.

```html
<!DOCTYPE html>
<html lang="en">
<head>
<meta charset="utf-8">
<title>Internal Process For Scanning Our Customer Records</title>
<link rel="stylesheet" href="https://fonts.googleapis.com/css2?family=Barlow:ital,wght@1,400&family=Inter:wght@600;700;800;900&display=swap">
<style>
  :root {
    --bg: #f4f4f4;
    --gold: #c4930a;
    --navy: #2e3192;
    --lavender: #c7c9f6;
    --wedge: #ebebeb;
    --white: #ffffff;
    --ink: #1b1b1b;
    --dot: #e0e0e0;
    --art-a: #d9dbfb;
    --art-b: #b9bdf2;
  }
  * { margin: 0; padding: 0; box-sizing: border-box; }
  html, body { width: 1200px; height: 606px; overflow: hidden; background: var(--bg); }
  .canvas {
    position: relative;
    width: 1200px;
    height: 606px;
    overflow: hidden;
    background: radial-gradient(circle at 30% 45%, #fbfbfb 0%, var(--bg) 70%);
    font-family: "Inter", sans-serif;
  }
  .backdrop { position: absolute; inset: 0; }
  .headline { position: absolute; left: 84px; top: 166px; }
  .headline__kicker {
    font-family: "Barlow", sans-serif;
    font-style: italic;
    font-weight: 400;
    font-size: 36px;
    line-height: 1;
    color: var(--gold);
    letter-spacing: 0.2px;
  }
  .headline__title {
    margin-top: 18px;
    font-family: "Inter", sans-serif;
    font-weight: 900;
    font-size: 60px;
    line-height: 63px;
    letter-spacing: -0.5px;
    color: var(--ink);
  }
  .step-label { font-family: "Inter", sans-serif; font-weight: 700; font-size: 11.5px; fill: var(--ink); }
  .step-number { font-family: "Inter", sans-serif; font-weight: 800; font-size: 27px; fill: var(--navy); }
  .brand-name { font-family: "Inter", sans-serif; font-weight: 800; font-size: 17px; fill: var(--navy); }
</style>
</head>
<body>
<div class="canvas">
  <svg class="backdrop" width="1200" height="606" viewBox="0 0 1200 606">
    <defs>
      <pattern id="dot-grid" width="12.4" height="12.4" patternUnits="userSpaceOnUse">
        <circle cx="3.5" cy="3.5" r="3.3" fill="var(--dot)"/>
      </pattern>
      <linearGradient id="art-fill" x1="0" y1="0" x2="1" y2="1">
        <stop offset="0" stop-color="var(--art-a)"/>
        <stop offset="1" stop-color="var(--art-b)"/>
      </linearGradient>
    </defs>

    <!-- decorative shapes -->
    <rect class="dots dots--top-left" x="84" y="2" width="124" height="62" fill="url(#dot-grid)"/>
    <rect class="dots dots--right" x="1140" y="67" width="62" height="124" fill="url(#dot-grid)"/>
    <path class="accent-diamond" d="M410 0 L650 0 L500 150 Q484 166 468 150 L386 68 Q369 51 386 34 Z" fill="var(--gold)"/>
    <circle class="accent-disc" cx="265" cy="646" r="190" fill="var(--navy)"/>
    <path class="accent-blob" d="M930 52 C1080 40 1210 120 1205 300 L1205 606 L690 606 C620 560 600 470 640 400 C660 340 700 300 720 230 C760 110 830 60 930 52 Z" fill="var(--lavender)"/>

    <!-- process wheel -->
    <g class="process-wheel">
      <circle cx="849" cy="303" r="240" fill="var(--white)"/>
      <circle cx="849" cy="303" r="222" fill="var(--wedge)"/>
      <g stroke="var(--white)" stroke-width="9">
        <line x1="849" y1="75" x2="849" y2="531"/>
        <line x1="621" y1="303" x2="1077" y2="303"/>
        <line x1="688" y1="142" x2="1010" y2="464"/>
        <line x1="1010" y1="142" x2="688" y2="464"/>
      </g>
      <circle cx="849" cy="303" r="73" fill="var(--white)"/>
      <circle class="hub-ring" cx="849" cy="303" r="60" fill="var(--white)" stroke="var(--navy)" stroke-width="6"/>
      <text class="brand-name" x="849" y="309" text-anchor="middle">Northfield</text>
    </g>

    <!-- step illustrations -->
    <g class="step-art" fill="url(#art-fill)" opacity="0.85">
      <rect x="890" y="77" width="112" height="72" rx="10" role="img" aria-label="Illustration: delivery truck with map pin and phone"/>
      <rect x="993" y="189" width="102" height="88" rx="10" role="img" aria-label="Illustration: team reviewing dashboards and inventory"/>
      <rect x="997" y="352" width="96" height="60" rx="10" role="img" aria-label="Illustration: people sorting binders and folders"/>
      <rect x="876" y="447" width="89" height="89" rx="10" role="img" aria-label="Illustration: document scan with magnifier and charts"/>
      <rect x="720" y="440" width="92" height="84" rx="10" role="img" aria-label="Illustration: person at laptop extracting data"/>
      <rect x="582" y="331" width="128" height="79" rx="10" role="img" aria-label="Illustration: laptop with star ratings for quality review"/>
      <rect x="589" y="179" width="126" height="77" rx="10" role="img" aria-label="Illustration: people handing over document boxes"/>
      <rect x="708" y="63" width="114" height="77" rx="10" role="img" aria-label="Illustration: secure records with lock and password screen"/>
    </g>

    <!-- step numbers -->
    <g class="step-numbers">
      <text class="step-number" x="868" y="135">1</text>
      <text class="step-number" x="994" y="198">2</text>
      <text class="step-number" x="1023" y="347">3</text>
      <text class="step-number" x="951" y="471">4</text>
      <text class="step-number" x="813" y="501">5</text>
      <text class="step-number" x="685" y="430">6</text>
      <text class="step-number" x="656" y="289">7</text>
      <text class="step-number" x="726" y="164">8</text>
    </g>

    <!-- step labels -->
    <g class="step-labels">
      <text class="step-label" x="865" y="173"><tspan x="865">TRANSPORT</tspan><tspan x="865" dy="14.5">DOCUMENTS</tspan></text>
      <text class="step-label" x="928" y="273"><tspan x="928">INVENTORY</tspan><tspan x="928" dy="14.5">RECORDS</tspan></text>
      <text class="step-label" x="928" y="341"><tspan x="928">DOCUMENT</tspan><tspan x="928" dy="14.5">PREPARATION</tspan></text>
      <text class="step-label" x="862" y="422"><tspan x="862">SCAN</tspan><tspan x="862" dy="14.5">DOCUMENTS</tspan></text>
      <text class="step-label" x="833" y="418" text-anchor="end"><tspan x="833">AI &amp; DATA</tspan><tspan x="833" dy="14.5">EXTRACTION</tspan></text>
      <text class="step-label" x="703" y="346"><tspan x="703">QUALITY</tspan><tspan x="703" dy="14.5">CONTROL</tspan></text>
      <text class="step-label" x="690" y="271"><tspan x="690">DELIVER</tspan><tspan x="690" dy="14.5">DOCUMENTS</tspan></text>
      <text class="step-label" x="755" y="165"><tspan x="755">RECORD</tspan><tspan x="755" dy="14.5">RETENTION &amp;</tspan><tspan x="755" dy="14.5">DESTRUCTION</tspan></text>
    </g>
  </svg>

  <header class="headline">
    <p class="headline__kicker">Internal Process For</p>
    <h1 class="headline__title">SCANNING<br>OUR CUSTOMER<br>RECORDS</h1>
  </header>
</div>
</body>
</html>
```